Freelance business trainer needs a new business card

My business is called Tbrite. I provide training in the workplace on management, coaching and mentoring, and customer service topics for a variety of businesses, colleges and private training providers, and teach on management programs. I need a professional but eye catching business card. Business colours grey and orange. My name Linda Marchbank; Tel 07853 416207; email lmarchbank@tbrite.co.uk; website www.tbrite.co.uk.
Happy to have some sort of logo on front and details on back or all on one side
Target Market(s)
SME businesses and colleges - workshops i run are for adults in the workplace
Industry/Entity Type
Training
Look and feel

```html
<!DOCTYPE html>
<html lang="en">
<head>
<meta charset="utf-8">
<title>Tbrite – Linda Marchbank business card</title>
<link rel="stylesheet" href="https://fonts.googleapis.com/css2?family=Cinzel:wght@400;600&family=Antonio:wght@300&display=swap">
<style>
  :root {
    --orange-light: #ff8c12;
    --orange-mid: #f77400;
    --orange-deep: #e85a00;
    --sun-yellow: #ffe600;
    --ink: #141414;
    --paper: #f2f2f2;
    --band-grey: #dfe3e3;
    --accent-red: #f0341a;
    --brown: #9a4a1a;
    --ornament: #c5621f;
  }
  html, body {
    margin: 0;
    padding: 0;
    width: 1200px;
    height: 720px;
    overflow: hidden;
    background: #ffffff;
  }
  .business-card {
    position: relative;
    width: 1200px;
    height: 720px;
    overflow: hidden;
    background:
      radial-gradient(ellipse 70% 60% at 50% 30%, var(--orange-light) 0%, var(--orange-mid) 60%, var(--orange-deep) 100%);
  }
  .brand-mark {
    position: absolute;
    left: 0;
    top: 70px;
    width: 1200px;
    text-align: center;
    font-family: "Cinzel", serif;
    font-weight: 600;
    font-size: 170px;
    line-height: 1;
    color: var(--sun-yellow);
  }
  .card-art {
    position: absolute;
    inset: 0;
  }
  .name-first { font-family: "Cinzel", serif; font-weight: 600; fill: var(--ink); }
  .name-last { font-family: "Cinzel", serif; font-weight: 400; fill: var(--paper); }
  .contact-band {
    position: absolute;
    left: 0;
    top: 562px;
    width: 1200px;
    height: 101px;
    background: var(--band-grey);
    border-top: 4px solid #d2590a;
    box-sizing: border-box;
  }
  .contact-label { fill: var(--accent-red); }
  .contact-value { fill: var(--ink); }
  .contact-line { font-family: "Antonio", sans-serif; font-weight: 300; font-size: 46px; }
  .footer-brand {
    position: absolute;
    left: 0;
    top: 676px;
    width: 1200px;
    text-align: center;
    font-family: "Cinzel", serif;
    font-weight: 400;
    font-size: 34px;
    line-height: 40px;
    color: var(--brown);
  }
  .flourish {
    position: absolute;
    top: 690px;
    width: 118px;
    height: 20px;
    border-radius: 10px;
    background: linear-gradient(90deg, rgba(197,98,31,0.15), var(--ornament), rgba(197,98,31,0.15));
  }
  .flourish--left { left: 384px; }
  .flourish--right { left: 725px; }
</style>
</head>
<body>
  <main class="business-card">
    <div class="brand-mark">Tbrite</div>

    <svg class="card-art" width="1200" height="720" viewBox="0 0 1200 720" aria-hidden="false">
      <defs>
        <filter id="name-shadow" x="-5%" y="-20%" width="110%" height="140%">
          <feDropShadow dx="3" dy="4" stdDeviation="3" flood-color="#7a3300" flood-opacity="0.55"/>
        </filter>
      </defs>
      <text class="holder-name" x="187" y="519" textLength="837" lengthAdjust="spacingAndGlyphs" font-size="112" filter="url(#name-shadow)"><tspan class="name-first">Linda </tspan><tspan class="name-last">Marchbank</tspan></text>
      <rect class="name-rule name-rule--dark" x="185" y="545" width="329" height="6" fill="#141414"/>
      <rect class="name-rule name-rule--light" x="514" y="545" width="508" height="6" fill="#f2f2f2"/>
    </svg>

    <div class="contact-band"></div>

    <svg class="card-art" width="1200" height="720" viewBox="0 0 1200 720">
      <text class="contact-line" x="19" y="636" textLength="1165" lengthAdjust="spacingAndGlyphs"><tspan class="contact-label">TEL:</tspan><tspan class="contact-value">07853 416207 </tspan><tspan class="contact-label">● EMAIL:</tspan><tspan class="contact-value">LMARCHBANK@TBRITE.CO.UK </tspan><tspan class="contact-label">● WEB:</tspan><tspan class="contact-value">WWW.TBRITE.CO.UK</tspan></text>
    </svg>

    <div class="flourish flourish--left" role="img" aria-label="Decorative scroll flourish"></div>
    <div class="footer-brand">Tbrite</div>
    <div class="flourish flourish--right" role="img" aria-label="Decorative scroll flourish"></div>
  </main>
</body>
</html>
```